Hi,

I have an event coming up for my nightclub Harlow On Finch called Zesto Fridays with the radio station Zesto FM,

I need a poster done up promoting the event, the date of the event is Friday the 25th of October at Harlow on Finch and also its featuring Zesto's own DJ Korvello.

You can add drink specials available on the night,

Open from 9pm till late

Requirements
Must have

```html
<!DOCTYPE html>
<html lang="en">
<head>
<meta charset="utf-8">
<title>Zesto Fridays at Harlow on Finch</title>
<link rel="stylesheet" href="https://fonts.googleapis.com/css2?family=Archivo+Black&family=Ubuntu:wght@400;500;700&display=swap">
<style>
  :root {
    --night: #120a1c;
    --plum: #3a1746;
    --magenta: #b04c9a;
    --orchid: #d98fd0;
    --salmon: #ec8a7c;
    --lavender: #dccbe9;
    --white: #ffffff;
    --floor: #1b1920;
  }
  html, body {
    margin: 0;
    padding: 0;
    overflow: hidden;
    background: var(--night);
  }
  .poster {
    position: relative;
    width: 857px;
    height: 1200px;
    overflow: hidden;
    background:
      radial-gradient(ellipse 520px 420px at 540px 330px, rgba(210, 90, 170, 0.55), transparent 70%),
      radial-gradient(ellipse 400px 500px at 120px 600px, rgba(120, 50, 150, 0.45), transparent 70%),
      linear-gradient(180deg, #1c0d26 0%, var(--plum) 45%, #2a1233 72%, var(--night) 100%);
    font-family: "Ubuntu", sans-serif;
  }
  .backdrop {
    position: absolute;
    inset: 0;
  }
  .model-photo {
    position: absolute;
    left: 240px;
    top: 0;
    width: 370px;
    height: 760px;
    border-radius: 180px 180px 40px 40px;
    background: radial-gradient(ellipse at 50% 35%, rgba(236, 170, 190, 0.85), rgba(170, 90, 150, 0.6) 55%, rgba(60, 25, 70, 0) 80%);
  }
  .venue-mark {
    position: absolute;
    left: 629px;
    top: 34px;
    width: 169px;
    height: 98px;
    background: #0c0a0e;
    border: 1px solid #6b4a78;
    display: flex;
    align-items: center;
    justify-content: center;
    color: var(--white);
    text-align: center;
  }
  .venue-mark__name {
    font-size: 17px;
    font-weight: 500;
    letter-spacing: 2px;
    line-height: 1.3;
  }
  .event-date {
    position: absolute;
    left: 45px;
    top: 182px;
    margin: 0;
    font-size: 31px;
    line-height: 44px;
    font-weight: 400;
    color: var(--salmon);
  }
  .floor {
    position: absolute;
    left: 0;
    top: 995px;
    width: 857px;
    height: 205px;
    background: linear-gradient(180deg, #24212b, var(--floor));
  }
  .title {
    position: absolute;
    left: 0;
    top: 630px;
  }
  .title-rule {
    position: absolute;
    left: 32px;
    top: 934px;
    width: 793px;
    height: 2px;
    background: linear-gradient(90deg, transparent, var(--orchid), var(--lavender), var(--orchid), transparent);
  }
  .subtitle {
    position: absolute;
    left: 0;
    width: 857px;
    top: 938px;
    text-align: center;
    font-size: 38px;
    font-weight: 700;
    letter-spacing: 2px;
    color: var(--lavender);
  }
  .featuring {
    position: absolute;
    left: 0;
    width: 857px;
    top: 1016px;
    text-align: center;
    font-size: 15px;
    letter-spacing: 11px;
    color: var(--white);
  }
  .station-name {
    position: absolute;
    left: 66px;
    top: 1062px;
    font-size: 28px;
    font-weight: 500;
    color: var(--white);
  }
  .headliner {
    position: absolute;
    left: 236px;
    top: 1046px;
    margin: 0;
    font-family: "Archivo Black", sans-serif;
    font-size: 64px;
    letter-spacing: -2px;
    font-weight: 400;
    color: var(--white);
  }
  .details {
    position: absolute;
    left: 0;
    width: 857px;
    top: 1136px;
    text-align: center;
    font-size: 29px;
    color: var(--white);
  }
</style>
</head>
<body>
<div class="poster">
  <svg class="backdrop" width="857" height="1200" viewBox="0 0 857 1200" aria-hidden="true">
    <g fill="#e6a0d8" opacity="0.12">
      <circle cx="140" cy="120" r="70"/>
      <circle cx="560" cy="80" r="55"/>
      <circle cx="720" cy="300" r="90"/>
      <circle cx="90" cy="460" r="60"/>
      <circle cx="660" cy="520" r="70"/>
      <circle cx="380" cy="520" r="40"/>
      <circle cx="800" cy="620" r="45"/>
      <circle cx="260" cy="300" r="35"/>
    </g>
    <g stroke="#ffffff" stroke-width="1.5" opacity="0.35">
      <line x1="310" y1="470" x2="760" y2="20"/>
      <line x1="260" y1="600" x2="820" y2="40"/>
      <line x1="330" y1="680" x2="850" y2="160"/>
      <line x1="230" y1="420" x2="640" y2="10"/>
    </g>
  </svg>

  <div class="model-photo" role="img" aria-label="Photo of a party-goer in sunglasses surrounded by glowing speakers"></div>

  <div class="venue-mark">
    <span class="venue-mark__name">HARLOW<br>ON FINCH</span>
  </div>

  <p class="event-date">Friday<br>the 25th<br>of October<br>at Harlow<br>on Finch</p>

  <div class="floor"></div>

  <svg class="title" width="857" height="290" viewBox="0 0 857 290" role="img" aria-label="zesto">
    <defs>
      <linearGradient id="titleFill" x1="0" y1="0" x2="1" y2="1">
        <stop offset="0" stop-color="#ffffff"/>
        <stop offset="0.35" stop-color="#f3c7ea"/>
        <stop offset="0.6" stop-color="#c65aa8"/>
        <stop offset="0.8" stop-color="#f6d7f0"/>
        <stop offset="1" stop-color="#b35a9c"/>
      </linearGradient>
    </defs>
    <text x="22" y="275" textLength="812" lengthAdjust="spacingAndGlyphs"
          font-family="Archivo Black, sans-serif" font-size="330"
          fill="url(#titleFill)" stroke="#4a1f52" stroke-width="2">zesto</text>
  </svg>

  <div class="title-rule"></div>
  <div class="subtitle">FRIDAYS</div>
  <div class="featuring">FEATURING</div>

  <div class="station-name">Zesto FM</div>
  <h1 class="headliner">DJ Korvello</h1>

  <div class="details">Specials available on the night / Open from 9pm till late</div>
</div>
</body>
</html>
```